Business Card Design for Law firm - already have logo

Now that we have a logo, we need a business card design - our logo is attached -it is salaryman font if that helps - we would like a file that can be uploaded to cardquill (www.cardquill-example.com) using the logo and with the following information on it:
Quenby Law Firm, P.C.
Delwyn Quenby, Esq.
5817 SW 19th Ave.
Portland, OR 97213
971.555.0142 phone
971.555.0187 fax
del@quenby-example.net
Skype: delquenby
Google talk: delwyn.quenby@mailbox-example.com
Target Market(s)
our business cards are distributed to corporate executives, technology professionals and healthcare providers
Industry/Entity Type
Business
Look and feel

```html
<!DOCTYPE html>
<html lang="en">
<head>
<meta charset="utf-8">
<title>Quenby Law Firm – Business Card</title>
<link rel="stylesheet" href="https://fonts.googleapis.com/css2?family=Sorts+Mill+Goudy&display=swap">
<style>
  :root {
    --teal: #2f6a67;
    --teal-dark: #285b58;
    --teal-soft: #8aa6a4;
    --stripe: #9fb2b1;
    --frame: #5f7f7e;
    --ink: #1f1f1f;
    --ink-grey: #6a6a6a;
    --paper: #ffffff;
  }
  * { margin: 0; padding: 0; box-sizing: border-box; }
  html, body {
    width: 1200px;
    height: 686px;
    overflow: hidden;
    background: var(--paper);
  }
  .card {
    position: relative;
    width: 1200px;
    height: 686px;
    font-family: "Sorts Mill Goudy", "Goudy Old Style", Georgia, serif;
    color: var(--ink);
    background: var(--paper);
  }
  .stripe-band {
    position: absolute;
    left: 0; top: 0;
    width: 1200px;
    height: 150px;
    background: repeating-linear-gradient(90deg, var(--stripe) 0 32px, var(--paper) 32px 64px);
    -webkit-mask-image: linear-gradient(to bottom, #000 0%, rgba(0,0,0,.55) 55%, transparent 100%);
            mask-image: linear-gradient(to bottom, #000 0%, rgba(0,0,0,.55) 55%, transparent 100%);
  }
  .card-body {
    position: absolute;
    left: 18px; top: 119px;
    width: 1164px; height: 549px;
    background: var(--paper);
    border-left: 2px solid var(--frame);
    border-right: 2px solid var(--frame);
    border-bottom: 2px solid var(--frame);
  }
  .crest {
    position: absolute;
    left: 526px; top: 32px;
    width: 146px; height: 56px;
    border-radius: 73px 73px 0 0;
    background: var(--teal-dark);
  }
  .crest-motif {
    position: absolute;
    left: 30px; top: 12px;
    width: 86px; height: 36px;
    border-radius: 50%;
    background: radial-gradient(ellipse at center, #e8efee 0%, #b9cccb 70%, var(--teal-soft) 100%);
  }
  .firm-banner {
    position: absolute;
    left: 149px; top: 85px;
    width: 898px; height: 107px;
    background: var(--paper);
    border: 4px solid var(--teal);
    display: flex;
    align-items: center;
    justify-content: center;
  }
  .firm-banner::before {
    content: "";
    position: absolute;
    inset: 7px;
    border: 1.5px solid var(--teal);
  }
  .firm-name {
    font-size: 46px;
    font-variant: small-caps;
    letter-spacing: 2px;
    color: var(--teal);
    font-weight: 400;
  }
  .contact-list {
    position: absolute;
    left: 73px; top: 346px;
    list-style: none;
    font-size: 28px;
    line-height: 43px;
    color: var(--ink);
  }
  .attorney {
    position: absolute;
    left: 704px; top: 252px;
    font-style: normal;
    font-size: 39px;
    line-height: 48px;
    color: var(--ink-grey);
  }
  .wordmark {
    position: absolute;
    left: 713px; top: 473px;
    width: 423px; height: 117px;
    display: flex;
    align-items: center;
    justify-content: center;
    font-size: 62px;
    letter-spacing: 14px;
    color: var(--ink);
  }
</style>
</head>
<body>
  <div class="card">
    <div class="stripe-band"></div>
    <div class="card-body"></div>

    <div class="crest">
      <div class="crest-motif" role="img" aria-label="Feather quill ornament"></div>
    </div>

    <header class="firm-banner">
      <h1 class="firm-name">Quenby Law Firm</h1>
    </header>

    <address class="attorney">
      Delwyn Quenby, Esq.<br>
      5817 SW 19th Ave.<br>
      Portland, OR 97213
    </address>

    <ul class="contact-list">
      <li>Phone: 971.555.0142</li>
      <li>Fax: 971.555.0187</li>
      <li>E-mail: del@quenby-example.net</li>
      <li>Skype: delquenby</li>
      <li>Google talk: delwyn.quenby@mailbox-example.com</li>
    </ul>

    <div class="wordmark">QUENBY</div>
  </div>
</body>
</html>
```